Paper Orchards (instructional dating book)

Title: Paper Orchards
Subtitle: Ways to charm a stranger across any crowded room
Author: R.J. Pollard
I'm seeking the title to be central with the subtitle underneath and the author slightly lower and to the left. Perhaps a border or two around the font. I thought the background could look aged (off color and old textured paper) and the background slightly punched into the texture like a typewriter has been used. I imagine it something like an old Fenwright playbook or 1940s morse code manual. Many thanks!

Target Market(s)

18 to 45 year old single people

Industry/Entity Type

Dating

Font styles to use
Serif

Requirements
Must have
• Text with border or two
Nice to have
• Traditional feel. The book is instructional.
Should not have
• Too much color or flair

```html
<!DOCTYPE html>
<html lang="en">
<head>
<meta charset="utf-8">
<title>Paper Orchards — R.J. Pollard</title>
<link rel="stylesheet" href="https://fonts.googleapis.com/css2?family=Special+Elite&family=Courier+Prime:wght@700&family=EB+Garamond:wght@400&display=swap">
<style>
  :root {
    --backdrop: #625659;
    --paper-light: #f2ece0;
    --paper-mid: #e7ddcc;
    --paper-shade: #d3c3a8;
    --stain: #a8834f;
    --ink-black: #1b1714;
    --ink-red: #641111;
    --rule: #5e3a30;
    --band-red: #470606;
    --band-text: #f4efe6;
  }
  html, body {
    margin: 0;
    padding: 0;
    width: 1200px;
    height: 776px;
    overflow: hidden;
    background: var(--backdrop);
  }
  .stage {
    position: relative;
    width: 1200px;
    height: 776px;
  }
  .cover {
    position: absolute;
    left: 365px;
    top: 50px;
    width: 470px;
    height: 676px;
    overflow: hidden;
    box-shadow: 0 6px 18px rgba(0,0,0,0.25);
  }
  .cover__paper {
    position: absolute;
    inset: 0;
    width: 470px;
    height: 676px;
  }
  .cover__title {
    position: absolute;
    left: 0;
    top: 0;
    width: 470px;
    height: 676px;
    margin: 0;
  }
  .cover__title-small {
    font-family: "Special Elite", "Courier Prime", "Courier New", monospace;
    font-size: 40px;
    fill: var(--ink-black);
  }
  .cover__title-large {
    font-family: "Special Elite", "Courier Prime", "Courier New", monospace;
    font-size: 84px;
    fill: var(--ink-red);
  }
  .cover__frame {
    fill: none;
    stroke: var(--rule);
    opacity: 0.55;
  }
  .cover__subtitle {
    position: absolute;
    left: 218px;
    top: 388px;
    margin: 0;
    font-family: "Courier Prime", "Courier New", monospace;
    font-weight: 700;
    font-size: 12.5px;
    line-height: 17px;
    color: var(--ink-black);
  }
  .cover__band {
    position: absolute;
    left: 0;
    bottom: 0;
    width: 100%;
    height: 57px;
    background: var(--band-red);
    display: flex;
    align-items: center;
    justify-content: center;
  }
  .cover__author {
    margin: 0;
    font-family: "EB Garamond", Georgia, serif;
    font-size: 29px;
    color: var(--band-text);
    letter-spacing: 0.5px;
  }
</style>
</head>
<body>
  <main class="stage">
    <section class="cover">
      <svg class="cover__paper" viewBox="0 0 470 676" role="img" aria-label="Aged, creased off-white paper texture with a central fold and faint stains">
        <defs>
          <radialGradient id="paper-tone" cx="50%" cy="45%" r="75%">
            <stop offset="0" stop-color="var(--paper-light)"/>
            <stop offset="0.65" stop-color="var(--paper-mid)"/>
            <stop offset="1" stop-color="var(--paper-shade)"/>
          </radialGradient>
          <filter id="paper-grain" x="0" y="0" width="100%" height="100%">
            <feTurbulence type="fractalNoise" baseFrequency="0.9" numOctaves="3" seed="4"/>
            <feColorMatrix values="0 0 0 0 0.45  0 0 0 0 0.36  0 0 0 0 0.24  0 0 0 0.22 0"/>
          </filter>
          <filter id="paper-blotch" x="0" y="0" width="100%" height="100%">
            <feTurbulence type="fractalNoise" baseFrequency="0.012" numOctaves="4" seed="9"/>
            <feColorMatrix values="0 0 0 0 0.55  0 0 0 0 0.42  0 0 0 0 0.25  0 0 0 0.35 -0.08"/>
          </filter>
          <linearGradient id="fold" x1="0" x2="1">
            <stop offset="0" stop-color="var(--stain)" stop-opacity="0"/>
            <stop offset="0.5" stop-color="var(--stain)" stop-opacity="0.5"/>
            <stop offset="1" stop-color="var(--stain)" stop-opacity="0"/>
          </linearGradient>
        </defs>
        <rect width="470" height="676" fill="url(#paper-tone)"/>
        <rect width="470" height="676" filter="url(#paper-blotch)"/>
        <rect width="470" height="676" filter="url(#paper-grain)"/>
        <rect x="275" y="0" width="8" height="676" fill="url(#fold)"/>
        <path d="M290 0 L282 30 L276 40" stroke="var(--stain)" stroke-width="1.5" fill="none" opacity="0.6"/>
      </svg>
      <svg class="cover__title" viewBox="0 0 470 676" role="heading" aria-level="1" aria-label="Paper Orchards">
        <defs>
          <filter id="ink-wear" x="-5%" y="-10%" width="110%" height="120%">
            <feTurbulence type="fractalNoise" baseFrequency="0.55" numOctaves="2" seed="3" result="noise"/>
            <feDisplacementMap in="SourceGraphic" in2="noise" scale="2.2" result="rough"/>
            <feColorMatrix in="noise" type="matrix" values="0 0 0 0 0  0 0 0 0 0  0 0 0 0 0  0 0 0 -3 2.1" result="holes"/>
            <feComposite in="rough" in2="holes" operator="in"/>
          </filter>
        </defs>
        <rect class="cover__frame" x="44" y="262" width="382" height="128" stroke-width="1"/>
        <rect class="cover__frame" x="49" y="267" width="372" height="118" stroke-width="0.6"/>
        <g filter="url(#ink-wear)">
          <text class="cover__title-small" x="84" y="309" textLength="146" lengthAdjust="spacingAndGlyphs">PAPER</text>
          <text class="cover__title-large" x="60" y="374" textLength="355" lengthAdjust="spacingAndGlyphs">ORCHARDS</text>
        </g>
      </svg>
      <p class="cover__subtitle">Ways to charm a stranger<br>across any crowded room</p>
      <footer class="cover__band">
        <p class="cover__author">R.J. Pollard</p>
      </footer>
    </section>
  </main>
</body>
</html>
```